New Email Marketing Design Project

I’d like you to make an email template. I’ll be welcoming and on boarding customers via email. And I’d like the branding to stand out. Keep it professional and simple. But be creative.

Design should look amazing on desktop and mobile phones.

Negative white space is ok.

Use stock images

I’ll like to have a spot for a picture of myself so make sure to include a circle where I can show my face so that email viewers will know who is speaking to them.

Target Market(s)

Practice managers, doctors, medical providers

Font styles to use
Sans Serif

Requirements
Must have
• Our Logo, CTA buttons, Same colors as website.
https://www.tavrenhealthclaims.com

```html
<!DOCTYPE html>
<html lang="en">
<head>
<meta charset="utf-8">
<title>Tavren Health Claims – Welcome Email</title>
<link rel="stylesheet" href="https://fonts.googleapis.com/css2?family=Montserrat:wght@300;400;600;700&family=Open+Sans:wght@600;700&display=swap">
<style>
  :root{
    --page:#f2f3f5;
    --white:#ffffff;
    --brand:#2e79a3;
    --brand-deep:#236a93;
    --tile-1:#0a8bc6;
    --tile-2:#2b79b6;
    --tile-3:#2e74a0;
    --ink:#2b2b2b;
    --banner:#2d2d2e;
    --body:#4a4a4a;
    --rail:#c9c9cb;
    --footer:#9b9b9d;
  }
  *{box-sizing:border-box;margin:0;padding:0}
  html,body{width:1200px;height:1014px;overflow:hidden;background:var(--page)}
  body{font-family:"Montserrat",sans-serif;color:var(--ink);position:relative}
  .email{position:absolute;left:230px;top:12px;width:739px;height:990px;
    background:linear-gradient(90deg,#d4d4d6 0,#f1f1f2 31px,var(--white) 31px,var(--white) 698px,#f2f2f3 698px,#c8c8ca 739px)}
  .header{position:absolute;left:0;top:0;width:739px;height:56px;background:var(--white);}
  .brand{position:absolute;left:46px;top:13px;display:flex;align-items:center;gap:14px}
  .brand-mark{width:26px;height:26px;border-radius:50%;border:2px solid var(--brand)}
  .brand-name{font-family:"Open Sans",sans-serif;font-weight:700;font-size:14px;color:var(--brand)}
  .hotline{position:absolute;left:410px;top:14px;display:flex;gap:8px;align-items:center}
  .hotline-label{font-size:7.5px;color:#333;line-height:1.3}
  .hotline-number{font-family:"Open Sans",sans-serif;font-weight:700;font-size:11px;color:#111}
  .cta{position:absolute;left:581px;top:11px;width:105px;height:27px;background:var(--brand);color:#fff;
    font-size:9.5px;font-weight:700;display:flex;align-items:center;justify-content:center;gap:5px;text-decoration:none;border:1px solid #b9d3e2}
  .hero{position:absolute;left:31px;top:56px;width:667px;height:400px}
  .title-banner{position:absolute;left:31px;top:436px;width:430px;height:80px;background:var(--banner);
    color:#fff;font-weight:700;font-size:50px;display:flex;align-items:center;padding-left:46px;letter-spacing:-.5px}
  .title-sub{position:absolute;left:78px;top:514px;font-weight:300;font-size:56px;color:var(--brand);letter-spacing:.5px}
  .section{position:absolute;left:77px;width:590px}
  .section h2{font-size:9px;font-weight:700;color:#111;margin-bottom:6px}
  .section p{font-size:8.6px;font-weight:600;line-height:16.5px;color:var(--body)}
  .about{top:578px}
  .read-more{display:inline-flex;margin-top:9px;border:1px solid var(--brand);color:var(--brand);font-size:5.5px;font-weight:700;padding:3px 5px}
  .features{position:absolute;left:77px;top:696px;width:590px;height:108px;display:flex}
  .feature{flex:1;display:flex;flex-direction:column;align-items:center;justify-content:center;gap:12px;color:#fff;text-align:center}
  .feature:nth-child(1){background:var(--tile-1)}
  .feature:nth-child(2){background:var(--tile-2)}
  .feature:nth-child(3){background:var(--tile-3)}
  .feature p{font-size:7px;line-height:9px;font-weight:600;width:120px}
  .remote{top:813px}
  .contacts{position:absolute;left:77px;top:902px;width:590px;display:flex;align-items:center;gap:14px;font-size:6.3px;font-weight:600;color:#333}
  .contact{display:flex;align-items:center;gap:6px}
  .footer{position:absolute;left:31px;top:949px;width:667px;height:41px;background:var(--footer);
    box-shadow:0 -6px 8px -4px rgba(0,0,0,.12)}
  .social{position:absolute;right:34px;top:9px;display:flex;gap:10px}
  .social span{width:24px;height:24px;border-radius:50%;border:1.5px solid #333}
</style>
</head>
<body>
<main class="email">
  <header class="header">
    <div class="brand"><span class="brand-mark"></span><span class="brand-name">Tavren Health Claims</span></div>
    <div class="hotline">
      <svg width="12" height="22" viewBox="0 0 12 22"><rect x="1" y="1" width="10" height="20" rx="2" fill="none" stroke="#2e79a3" stroke-width="2"/><circle cx="6" cy="17.5" r="1.2" fill="#2e79a3"/></svg>
      <div><div class="hotline-label">Need Help? Call Us Now</div><div class="hotline-number">15550148822</div></div>
    </div>
    <a class="cta" href="https://www.tavrenhealthclaims.com">GET IN TOUCH
      <svg width="9" height="9" viewBox="0 0 10 10"><circle cx="5" cy="5" r="5" fill="#fff"/><path d="M4 3l2 2-2 2" stroke="#2e79a3" stroke-width="1.4" fill="none"/></svg></a>
  </header>

  <svg class="hero" viewBox="0 0 667 400">
    <defs>
      <clipPath id="col"><rect width="667" height="400"/></clipPath>
      <linearGradient id="desk" x1="0" y1="0" x2="1" y2="1">
        <stop offset="0" stop-color="#c9d9e8"/><stop offset=".45" stop-color="#eef1f3"/><stop offset="1" stop-color="#8e979f"/>
      </linearGradient>
      <linearGradient id="doc" x1="0" y1="0" x2="0" y2="1">
        <stop offset="0" stop-color="#e4e8ec"/><stop offset="1" stop-color="#cfd8e0"/>
      </linearGradient>
    </defs>
    <g clip-path="url(#col)">
      <circle cx="198" cy="120" r="258" fill="none" stroke="var(--brand)" stroke-width="12"/>
      <circle cx="207" cy="118" r="248" fill="#fff"/>
      <circle cx="200" cy="118" r="244" fill="url(#desk)" role="img" aria-label="Stock photo of hands writing in a notebook beside a laptop"/>
    </g>
    <circle cx="489" cy="250" r="116" fill="#fff" stroke="var(--brand)" stroke-width="5"/>
    <circle cx="489" cy="250" r="109" fill="url(#doc)" role="img" aria-label="Portrait photo spot for the sender"/>
  </svg>

  <div class="title-banner">Tavren Health</div>
  <div class="title-sub">Claims</div>

  <section class="section about">
    <h2>ABOUT US</h2>
    <p>At Tavren Health Claims we are focused on providing medical billing services with the highest levels of customer satisfaction &amp; we will do everything we can to meet your expectations. With a variety of offerings to choose from, we’re sure you’ll be happy working with us. Tavren Health Claims is a company that you can place your trust in. We offer comprehensive and secure billing support</p>
    <a class="read-more" href="https://www.tavrenhealthclaims.com">READ MORE ›</a>
  </section>

  <div class="features">
    <div class="feature">
      <svg width="30" height="28" viewBox="0 0 30 28"><circle cx="15" cy="8" r="7" fill="#fff"/><path d="M2 28c0-9 6-12 13-12s13 3 13 12z" fill="#fff"/></svg>
      <p>Lorem ipsum dolor sit amet, qu ix el idque intellegat referren</p>
    </div>
    <div class="feature">
      <svg width="28" height="28" viewBox="0 0 28 28"><circle cx="17" cy="11" r="8" fill="none" stroke="#fff" stroke-width="3"/><path d="M11 17L3 25" stroke="#fff" stroke-width="4" stroke-linecap="round"/></svg>
      <p>Lorem ipsum dolor sit amet, qu ix el idque intellegat referren</p>
    </div>
    <div class="feature">
      <svg width="30" height="28" viewBox="0 0 30 28"><path d="M15 2L1 15h4v12h8v-8h4v8h8V15h4z" fill="#fff"/></svg>
      <p>Lorem ipsum dolor sit amet, qu ix el idque intellegat referren</p>
    </div>
  </div>

  <section class="section remote">
    <h2>REMOTE MEDICAL BILLING WORK ON THE RISE</h2>
    <p>Remote medical billing work on the rise thanks to COVID-19. Most people are not ready to risk bringing contagion home to their families. Rightfully so, they are choosing to not work at places where there are large crowds or many customers. Preferring smaller less trafficked setting. The trend is only going to continue as new platforms are made available every single week. It has been determined that outsourcing is the way of the future for medical billing. Is your practice on</p>
  </section>

  <div class="contacts">
    <div class="contact"><svg width="14" height="18" viewBox="0 0 14 18"><path d="M7 0a7 7 0 0 0-7 7c0 5 7 11 7 11s7-6 7-11a7 7 0 0 0-7-7z" fill="var(--brand)"/><circle cx="7" cy="7" r="2.5" fill="#fff"/></svg><span>210 Harbor Ave Ste 400<br>Lakeview, Oregon 97002</span></div>
    <div class="contact"><svg width="10" height="18" viewBox="0 0 10 18"><rect x="1" y="1" width="8" height="16" rx="1.5" fill="none" stroke="var(--brand)" stroke-width="1.6"/></svg><span>555-014-8822</span></div>
    <div class="contact"><svg width="18" height="16" viewBox="0 0 18 16"><rect x="0" y="5" width="18" height="11" rx="1" fill="var(--brand)"/><rect x="4" y="0" width="10" height="6" fill="var(--brand)"/><rect x="3" y="9" width="12" height="1.5" fill="#fff"/></svg><span>555-014-8822</span></div>
    <div class="contact"><svg width="18" height="12" viewBox="0 0 18 12"><rect width="18" height="12" fill="var(--brand)"/><path d="M0 0l9 7 9-7" stroke="#fff" stroke-width="1.4" fill="none"/></svg><span>hello@tavrenhealthclaims.com</span></div>
  </div>

  <footer class="footer">
    <div class="social"><span></span><span></span><span></span><span></span></div>
  </footer>
</main>
</body>
</html>
```